Doctors clinic requires stationary designed

We require various types of stationary to be design based on the logo (attached). We require the following:
- Letterhead (A4 Portrait)
- Business Card (must include UV spot on rear)
- With compliments slip (DL Landscape)
- Appointments card (Folded A6)

We are a young clinical practice which boasts a modern and sophisticated approach to medicine so we require something which feels fresh and modern. Please include colours represented in the logo (contrasting teal and grey). We are calling for creative minds to put forth their ideas and we will be actively providing feedback on all designs.

thank you

Clinic

```html
<!DOCTYPE html>
<html lang="en">
<head>
<meta charset="utf-8">
<title>Dr Clara Whitfield – Business Card</title>
<link rel="stylesheet" href="https://fonts.googleapis.com/css2?family=Source+Sans+3:wght@400;600;700&display=swap">
<style>
  :root {
    --backdrop: #e9e7e3;
    --card: #eeeeee;
    --teal: #1a8a85;
    --grey: #4a4a4a;
    --text: #5a5a5a;
    --shadow: rgba(0,0,0,0.12);
  }
  * { box-sizing: border-box; margin: 0; padding: 0; }
  html, body {
    width: 1200px; height: 900px; overflow: hidden;
    background: var(--backdrop);
    font-family: "Source Sans 3", "Myriad Pro", Arial, sans-serif;
  }
  .stage {
    width: 1200px; height: 900px;
    display: flex; align-items: center; justify-content: center; gap: 60px;
  }
  .card {
    width: 525px; height: 320px;
    background: var(--card);
    box-shadow: 0 8px 24px var(--shadow), 0 1px 3px var(--shadow);
    position: relative;
  }
  .card-front {
    display: flex; align-items: center; justify-content: center; gap: 12px;
  }
  .card-front .mark-dot {
    width: 26px; height: 26px; border: 3px solid var(--grey); border-radius: 50%;
  }
  .card-front .mark-name {
    font-size: 26px; font-weight: 600; color: var(--grey); letter-spacing: 0.5px;
  }
  .card-back { padding: 48px 0 0 44px; }
  .brand { display: flex; align-items: center; gap: 14px; }
  .brand-dot {
    width: 60px; height: 60px; border: 2.5px solid var(--teal); border-radius: 50%;
  }
  .brand-name {
    font-size: 26px; font-weight: 600; color: var(--teal); line-height: 1;
  }
  .brand-role {
    font-size: 15px; font-weight: 600; color: var(--teal); margin-top: 4px;
  }
  .address {
    margin-top: 26px; font-size: 15px; color: var(--text); line-height: 1.3;
  }
  .contact-list { list-style: none; margin-top: 8px; }
  .contact-list li {
    display: flex; align-items: center; gap: 12px;
    font-size: 15px; color: var(--text); line-height: 1.35;
  }
  .contact-list svg { width: 13px; height: 13px; fill: var(--teal); flex: none; }
  .contact-list .web { font-weight: 700; color: var(--grey); }
</style>
</head>
<body>
<main class="stage">
  <section class="card card-front" aria-label="Business card front">
    <span class="mark-dot"></span>
    <span class="mark-name">Dr Clara Whitfield</span>
  </section>

  <section class="card card-back" aria-label="Business card back">
    <div class="brand">
      <span class="brand-dot"></span>
      <div>
        <div class="brand-name">Dr Clara Whitfield</div>
        <div class="brand-role">Obstetrician and Gynaecologist</div>
      </div>
    </div>
    <address class="address" style="font-style:normal">
      Harbourside Private Hospital<br>
      Suite 4, Westgate Medical Centre<br>
      Marlow Ave, Eastbrook WA 6199
    </address>
    <ul class="contact-list">
      <li>
        <svg viewBox="0 0 16 16" aria-label="Phone"><path d="M4 1l3 3-1.5 2a9 9 0 0 0 4.5 4.5L12 9l3 3-2 3C7 15 1 9 1 3z"/></svg>
        9555 0140
      </li>
      <li>
        <svg viewBox="0 0 16 16" aria-label="Fax"><path d="M4 1h7v4H4zM1 6h14v8H1zm3 4h8v1H4z"/></svg>
        9555 0147
      </li>
      <li>
        <svg viewBox="0 0 16 16" aria-label="Email"><path d="M1 3h14v10H1zm1 1.5v.5l6 4 6-4v-.5z" fill-rule="evenodd"/></svg>
        info@drclarawhitfield.com.au
      </li>
      <li class="web">
        <svg viewBox="0 0 16 16" aria-label="Website"><circle cx="8" cy="8" r="7"/></svg>
        drclarawhitfield.com.au
      </li>
    </ul>
  </section>
</main>
</body>
</html>
```